Beacon Advisory Website

I currently have a website www.beaconadvisoryinc.example. We are a IT Consulting Company. Our website will pretty much tell out our services. I am looking to enhance my website and make it look more professional. Looking for very classy and Contemporary look and design for my website.

Industry/Entity Type

It Company

```html
<!DOCTYPE html>
<html lang="en">
<head>
<meta charset="utf-8">
<title>Beacon Advisory</title>
<link href="https://fonts.googleapis.com/css2?family=Montserrat:wght@300;400;600;700&family=Open+Sans:wght@400;600&display=swap" rel="stylesheet">
<style>
:root{
  --blue:#1565a8;
  --ink:#3a3a3a;
  --text:#666;
  --muted:#999;
  --line:#e5e5e5;
  --footer:#333333;
  --footer-bar:#232323;
  --white:#fff;
  --dark-btn:#2d2d2d;
}
*{margin:0;padding:0;box-sizing:border-box}
html,body{width:1200px;height:2256px;overflow:hidden;background:var(--white)}
body{position:relative;font-family:"Open Sans",Arial,sans-serif;color:var(--text)}
.abs{position:absolute}
/* header */
.site-header{position:absolute;left:0;top:0;width:1200px;height:56px;background:var(--white)}
.brand{left:270px;top:9px;display:flex;align-items:center;gap:8px}
.brand-mark{width:38px;height:38px;border-radius:50%;background:var(--blue)}
.brand-name{font-family:"Montserrat",sans-serif;font-weight:700;font-size:16px;color:var(--blue);line-height:1}
.brand-name small{display:block;font-weight:400;font-size:9px;letter-spacing:2px;color:var(--blue);margin-top:2px}
.main-nav{left:573px;top:21px;display:flex;gap:0;font-size:9px;letter-spacing:.3px;color:#666}
.main-nav span{margin-right:29px}
.main-nav .active{color:var(--blue)}
/* hero */
.hero{left:0;top:56px;width:1200px;height:319px;background:linear-gradient(90deg,#4a4c50 0%,#8e8f92 35%,#b9b7b3 60%,#9c9a98 80%,#5e5f62 100%)}
.hero-title{left:0;width:1200px;top:190px;text-align:center;font-family:"Montserrat",sans-serif;font-weight:300;font-size:24px;color:var(--white);letter-spacing:1px}
.hero-sub{left:0;width:1200px;top:223px;text-align:center;font-size:14px;color:var(--white)}
.hero-arrow{top:206px}
/* intro */
.section-title{left:0;width:1200px;text-align:center;font-family:"Montserrat",sans-serif;font-weight:300;font-size:17px;color:#555;letter-spacing:.5px}
.section-title b{font-weight:600}
.rule{height:3px;width:34px;background:var(--blue)}
.intro-text{left:375px;width:450px;top:487px;text-align:center;font-size:9px;line-height:17px;color:#666}
.feature{top:553px;width:210px;height:195px;padding:38px 0 0 0}
.feature h3{font-family:"Open Sans",sans-serif;font-weight:600;font-size:12px;color:#555;margin-top:14px;letter-spacing:.3px}
.feature p{font-size:9px;color:#777;margin-top:6px}
.feature .more{display:inline-block;font-size:7px;color:#888;margin-top:16px;letter-spacing:.3px}
.feature.highlight{background:var(--blue);padding-left:40px}
.feature.highlight h3,.feature.highlight p,.feature.highlight .more{color:var(--white)}
.feature.highlight .more{border-bottom:1px solid var(--white);padding-bottom:5px}
.divider{left:270px;top:808px;width:660px;height:1px;background:var(--line)}
/* about */
.about-title{left:270px;top:851px;font-family:"Montserrat",sans-serif;font-weight:400;font-size:17px;color:#444}
.about-lead{left:270px;top:884px;width:290px;font-size:10px;font-weight:600;line-height:18px;color:var(--blue)}
.about-body{left:270px;top:931px;width:290px;font-size:9px;line-height:16px;color:#666}
.btn-more{left:270px;top:1071px;height:27px;display:flex}
.btn-more .label{background:var(--blue);color:var(--white);font-size:9px;letter-spacing:.5px;width:78px;display:flex;align-items:center;justify-content:center}
.btn-more .go{background:var(--dark-btn);width:30px;display:flex;align-items:center;justify-content:center}
.service{width:160px}
.service h4{font-family:"Montserrat",sans-serif;font-weight:400;font-size:12px;color:#555;margin-top:4px}
.service .rule{width:24px;height:2px;margin:10px 0 12px}
.service p{font-size:9px;line-height:15px;color:#777}
/* career */
.career{left:0;top:1254px;width:1200px;height:336px;background:linear-gradient(90deg,#1f3443 0%,#3d5566 40%,#6c7b85 70%,#8a9297 100%)}
.career-title{left:270px;top:1362px;font-family:"Montserrat",sans-serif;font-weight:300;font-size:24px;color:var(--white);letter-spacing:.5px}
.career-sub{left:272px;top:1406px;font-size:13px;font-weight:600;line-height:19px;color:var(--white);letter-spacing:.3px}
.btn-outline{left:270px;top:1471px;width:117px;height:31px;border:1px solid var(--white);color:var(--white);font-size:8px;letter-spacing:1px;display:flex;align-items:center;justify-content:center}
/* clients */
.clients-title{left:0;width:1200px;top:1635px;text-align:center;font-family:"Montserrat",sans-serif;font-weight:300;font-size:20px;color:#666}
.clients-text{left:390px;width:420px;top:1670px;text-align:center;font-size:10px;line-height:15px;color:#999}
.client-row{left:300px;top:1732px;width:600px;display:flex;justify-content:space-between;align-items:center}
.client{font-family:"Montserrat",sans-serif;font-weight:600;font-size:19px;color:#666;display:flex;align-items:center;gap:6px}
.client i{display:inline-block;width:10px;height:10px;border-radius:50%;background:#888}
/* footer */
.site-footer{left:0;top:1818px;width:1200px;height:394px;background:var(--footer)}
.footer-title{font-family:"Montserrat",sans-serif;font-weight:400;font-size:15px;color:var(--white);letter-spacing:.5px}
.footer-text{left:270px;top:1917px;width:300px;font-size:9px;line-height:16px;color:#aaa}
.contact-line{left:270px;display:flex;align-items:center;gap:14px;font-size:11px;color:#ddd;line-height:16px}
.contact-line .circle{width:23px;height:23px;border:1.5px solid #bbb;border-radius:50%;display:flex;align-items:center;justify-content:center;flex:none}
.field{left:630px;width:300px;border:1px solid #4a4a4a;font-size:9px;color:#999;padding:9px 14px}
.send{left:630px;top:2134px;width:300px;height:35px;background:var(--white);color:#333;font-size:10px;letter-spacing:.5px;display:flex;align-items:center;justify-content:center}
.footer-bar{left:0;top:2212px;width:1200px;height:44px;background:var(--footer-bar)}
.copyright{left:270px;top:2227px;font-size:8px;color:#aaa}
.socials{left:849px;top:2223px;display:flex;gap:5px}
.socials span{width:17px;height:17px;border:1px solid #ccc;border-radius:50%}
</style>
</head>
<body>

<header class="site-header">
  <div class="abs brand">
    <span class="brand-mark"></span>
    <span class="brand-name">BEACON<small>ADVISORY</small></span>
  </div>
  <nav class="abs main-nav">
    <span class="active">COMPANY</span><span>SOLUTION</span><span>SERVICES</span><span>RESOURCES</span><span>CAREER</span><span>CONTACT US</span>
  </nav>
</header>

<section class="abs hero" role="img" aria-label="Photo of business consultants reviewing documents at a laptop"></section>
<div class="abs hero-title">CONSULTING</div>
<div class="abs hero-sub">Focus on enhancing business performance</div>
<svg class="abs hero-arrow" style="left:154px" width="14" height="26" viewBox="0 0 14 26"><path d="M12 2 2 13l10 11" fill="none" stroke="#fff" stroke-width="2"/></svg>
<svg class="abs hero-arrow" style="left:1018px" width="14" height="26" viewBox="0 0 14 26"><path d="M2 2l10 11L2 24" fill="none" stroke="#2f7bc4" stroke-width="2"/></svg>

<h2 class="abs section-title" style="top:441px">WE ARE <b>BEACON ADVISORY</b></h2>
<div class="abs rule" style="left:583px;top:474px"></div>
<p class="abs intro-text">Lorem Ipsum is simply dummy text of the printing and typesetting industry. Lorem Ipsum has been the industry's standard dummy text ever since the 1500s, when an unknown printer took a galley</p>

<div class="abs feature" style="left:278px">
  <svg width="40" height="26" viewBox="0 0 40 26"><path d="M2 8l10-5 8 4 8-4 10 5-6 10-8 5-8-5z" fill="#888"/></svg>
  <h3>CONSULTING</h3>
  <p>Beacon Advisory has certified professional</p>
  <span class="more">READ MORE</span>
</div>
<div class="abs feature highlight" style="left:490px;padding-left:40px">
  <svg width="40" height="26" viewBox="0 0 40 26"><rect x="1" y="6" width="22" height="13" fill="#fff"/><rect x="8" y="20" width="8" height="3" fill="#fff"/><circle cx="31" cy="8" r="5" fill="#fff"/><path d="M23 24c0-7 4-10 8-10s8 3 8 10z" fill="#fff"/></svg>
  <h3>STAFF AUGMENTATION</h3>
  <p>For years Beacon Advisory as been</p>
  <span class="more">READ MORE</span>
</div>
<div class="abs feature" style="left:744px">
  <svg width="32" height="32" viewBox="0 0 32 32"><circle cx="16" cy="16" r="6" fill="none" stroke="#888" stroke-width="1.5"/><circle cx="16" cy="16" r="12" fill="none" stroke="#888" stroke-width="1.5" stroke-dasharray="5 4"/></svg>
  <h3>OFFSHORE</h3>
  <p>Our Offshore development model</p>
  <span class="more">READ MORE</span>
</div>

<div class="abs divider"></div>

<h2 class="abs about-title">ABOUT US</h2>
<p class="abs about-lead">Lorem ipsum dolor sit amet, consectetuer adipiscing elit. Aenean commodo ligula eget dolor. Aenean massa.</p>
<p class="abs about-body">Today's IT market is a dynamic, fast-paced industry, with ever-increasing demands. Meeting these demands for over 25 years, Beacon Advisory maintains a global presence, aggressively recruiting expertly qualified IT and Management Professionals from around the world and cultivating key partnerships with corporations to understand their business models end-to-end, with a goal of delivering exceptional client service and ensuring a consistent delivery of the talent needed to drive results.</p>
<div class="abs btn-more"><span class="label">READ MORE</span><span class="go"><svg width="7" height="10" viewBox="0 0 7 10"><path d="M1 1l4 4-4 4" fill="none" stroke="#fff" stroke-width="1.5"/></svg></span></div>

<div class="abs service" style="left:602px;top:857px">
  <svg width="26" height="26" viewBox="0 0 26 26"><g fill="#555"><circle cx="13" cy="13" r="4"/><circle cx="4" cy="4" r="3"/><circle cx="22" cy="4" r="3"/><circle cx="4" cy="22" r="3"/><circle cx="22" cy="22" r="3"/></g><path d="M4 4l18 18M22 4 4 22" stroke="#555" stroke-width="1.5"/></svg>
  <h4>Technology</h4><div class="rule"></div>
  <p>Beacon Advisory Training programs are perfect for individuals</p>
</div>
<div class="abs service" style="left:791px;top:857px">
  <svg width="26" height="26" viewBox="0 0 26 26"><rect x="2" y="3" width="22" height="15" fill="none" stroke="#555" stroke-width="2"/><rect x="9" y="20" width="8" height="3" fill="#555"/><path d="M9 7l8 7M17 7l-8 7" stroke="#555" stroke-width="1.5"/></svg>
  <h4>Application Development</h4><div class="rule"></div>
  <p>Drawing on our experience in all major industries, we develop</p>
</div>
<div class="abs service" style="left:602px;top:975px">
  <svg width="26" height="26" viewBox="0 0 26 26"><path d="M8 22 20 8a4 4 0 0 0-6-5L4 16a3 3 0 0 0 4 4l9-10" fill="none" stroke="#555" stroke-width="2"/></svg>
  <h4>Business</h4><div class="rule"></div>
  <p>Our Offshore development model has a unique distinction</p>
</div>
<div class="abs service" style="left:791px;top:975px">
  <svg width="26" height="26" viewBox="0 0 26 26"><circle cx="10" cy="10" r="8" fill="none" stroke="#555" stroke-width="2"/><path d="M16 16l8 8M10 6v8M6 10h8" stroke="#555" stroke-width="2"/></svg>
  <h4>Enterprise Integration</h4><div class="rule"></div>
  <p>As organizations work to achieve and sustain competitive advantage</p>
</div>
<div class="abs service" style="left:602px;top:1100px">
  <svg width="28" height="22" viewBox="0 0 28 22"><path d="M1 6l8-4 6 3 6-3 6 4-5 9-7 5-7-5z" fill="#777"/></svg>
  <h4>IT Consulting</h4><div class="rule"></div>
  <p>Our Offshore development model has a unique distinction</p>
</div>

<section class="abs career" role="img" aria-label="Blurred photo of a desk with a laptop keyboard and glasses"></section>
<h2 class="abs career-title">IN YOUR GREAT CAREER</h2>
<p class="abs career-sub">WE ARE ONE OF THE LARGEST PROVIDERS OF THE LEADING<br>BUSINESS STRATEGIES!</p>
<div class="abs btn-outline">READ MORE</div>

<h2 class="abs clients-title">Our Happy Clients</h2>
<p class="abs clients-text">Lorem ipsum dolor sit amet, consectetuer adipiscing elit, sed diam nonummy nibh euismod tincidunt ut laoreet dolore magna aliquam erat volutpat.</p>
<div class="abs client-row">
  <span class="client">NORVALE</span>
  <span class="client">KEYSTRAND</span>
  <span class="client">ARCLINE</span>
  <span class="client">TESSIA</span>
  <span class="client">Halvik</span>
</div>

<footer class="abs site-footer"></footer>
<h3 class="abs footer-title" style="left:270px;top:1880px">CONTACT US</h3>
<p class="abs footer-text">Duis aute irure dolor in reprehenderit in voluptate velit esse cillum dolore eu fugiat nulla pariatur. Excepteur sint occaecat cupidatat</p>
<div class="abs contact-line" style="top:1982px">
  <span class="circle"><svg width="9" height="12" viewBox="0 0 9 12"><path d="M4.5 11S1 6.5 1 4.5a3.5 3.5 0 0 1 7 0C8 6.5 4.5 11 4.5 11z" fill="none" stroke="#ccc" stroke-width="1.2"/><circle cx="4.5" cy="4.5" r="1.2" fill="#ccc"/></svg></span>
  <span style="font-size:10px">418 Harbor Lane Suite 12, Millbrook,<br>NJ 07999</span>
</div>
<div class="abs contact-line" style="top:2030px">
  <span class="circle"><svg width="12" height="10" viewBox="0 0 12 10"><path d="M1 4c3-3 7-3 10 0l-2 2-2-1V3H5v2L3 6z" fill="#ccc"/></svg></span>
  <span style="font-size:13px">+1 (555) 014 2290</span>
</div>
<div class="abs contact-line" style="top:2079px">
  <span class="circle"><svg width="11" height="8" viewBox="0 0 11 8"><rect x=".5" y=".5" width="10" height="7" fill="none" stroke="#ccc"/><path d="M.5.5l5 4 5-4" fill="none" stroke="#ccc"/></svg></span>
  <span style="font-size:11px">info@beaconadvisory.example</span>
</div>

<h3 class="abs footer-title" style="left:630px;top:1880px">LEAVE A MESSAGE</h3>
<div class="abs field" style="top:1915px;height:31px">Your Name*</div>
<div class="abs field" style="top:1954px;height:33px">Your Email Address*</div>
<div class="abs field" style="top:1994px;height:32px">Phone Number</div>
<div class="abs field" style="top:2038px;height:84px">Message*</div>
<div class="abs send">SEND MESSAGE</div>

<div class="abs footer-bar"></div>
<p class="abs copyright">© All Right Reserved 2016. Beacon Advisory</p>
<div class="abs socials"><span></span><span></span><span></span><span></span></div>

</body>
</html>
```